Professional/modern business card design for construction company

We need a new business card design, double sided keeping it modern, sleek, professional and simple. We are an earthmoving business but do not want any pictures of machinery. I would like one side to have the logo and the other to have all the information, keeping with the colors in our logo. The business card will need to be able to be customised so we can use it for several different managers., we would also like to be able to use the design to apply it to other stationary ie. letterheads, notebooks etc. We do not really have a tag line but we could put on there that we specialise in - Agriculture, Civil Construction and Mining.

Contact Information for Business Card

Balgo Groundworks Pty Ltd
ABN 58 402 917 364
82 Dunmore Creek Road, Corrinvale NSW 2396

Desmond Fairweather
Managing Director
P 0438 614 205
E desfairweather@balgogroundworks.com.au

Font styles to use
Serif
Sans Serif

Requirements
Nice to have
• I have attached some examples of ideas.
Should not have
• images of machinery

```html
<!DOCTYPE html>
<html lang="en">
<head>
<meta charset="utf-8">
<title>Balgo Groundworks – Business Card</title>
<link rel="stylesheet" href="https://fonts.googleapis.com/css2?family=Montserrat:wght@500;600&family=Lato:wght@400&display=swap">
<style>
  :root {
    --backdrop: #2a2a2a;
    --card-light: #ffffff;
    --card-dark: #3d3d3d;
    --ink-dark: #3b3b3b;
    --ink-body: #2e2e2e;
    --ink-light: #f2f2f2;
    --ink-muted: #d6d6d6;
    --accent: #f28a1c;
    --rule-light: #9a9a9a;
    --rule-dark: #8a8a8a;
  }
  * { margin: 0; padding: 0; box-sizing: border-box; }
  html, body { width: 1200px; height: 1200px; overflow: hidden; }
  body { background: var(--backdrop); position: relative; font-family: "Lato", sans-serif; }

  .card { position: absolute; top: 310px; width: 366px; height: 594px; }
  .card--front { left: 234px; background: var(--card-light); }
  .card--back { left: 628px; width: 368px; background: var(--card-dark); }

  .centered { position: absolute; left: 0; right: 0; text-align: center; }

  .brand-name {
    font-family: "Montserrat", sans-serif; font-weight: 600;
    text-align: center; line-height: 1; letter-spacing: 0.5px;
  }
  .brand-name__main { display: block; }
  .brand-name__sub { display: block; margin-top: 12px; }
  .card--front .brand-name { color: var(--ink-dark); }
  .card--front .brand-name__main { font-size: 58px; }
  .card--front .brand-name__sub { font-size: 18px; }
  .card--back .brand-name { color: var(--card-light); }
  .card--back .brand-name__main { font-size: 62px; }
  .card--back .brand-name__sub { font-size: 19px; }

  .person-name {
    font-family: "Montserrat", sans-serif; font-weight: 600;
    color: var(--accent); font-size: 20px; line-height: 1;
  }
  .person-role { color: var(--ink-body); font-size: 17px; line-height: 1; }

  .icon-row { position: absolute; top: 362px; left: 87px; width: 190px; height: 26px; }

  .contact-list { color: var(--ink-body); font-size: 16.5px; line-height: 21.5px; }
  .rule { position: absolute; height: 1px; }
  .card--front .rule { background: var(--rule-light); }
  .card--back .rule { background: var(--rule-dark); }

  .company-label, .specialty-label {
    font-family: "Montserrat", sans-serif; font-weight: 600;
    color: var(--accent); font-size: 16.5px; line-height: 1;
  }
  .address { color: var(--ink-body); font-size: 17px; line-height: 22px; }

  .abn { font-size: 16.5px; color: var(--ink-muted); line-height: 1; }
  .abn__label { color: var(--accent); }
  .specialties { color: var(--ink-light); font-size: 17px; line-height: 22px; }
</style>
</head>
<body>

  <section class="card card--front" aria-label="Business card, contact side">
    <div class="brand-name centered" style="top:130px;">
      <span class="brand-name__main">BALGO</span>
      <span class="brand-name__sub">GROUNDWORKS PTY LTD</span>
    </div>

    <p class="person-name centered" style="top:311px;">DESMOND FAIRWEATHER</p>
    <p class="person-role centered" style="top:333px;">Managing Director</p>

    <svg class="icon-row" viewBox="0 0 190 26" aria-hidden="true">
      <line x1="0" y1="13" x2="56" y2="13" stroke="#9a9a9a" stroke-width="1"/>
      <line x1="134" y1="13" x2="190" y2="13" stroke="#9a9a9a" stroke-width="1"/>
      <circle cx="68" cy="13" r="12" fill="#f28a1c"/>
      <circle cx="95" cy="13" r="12" fill="#f28a1c"/>
      <circle cx="122" cy="13" r="12" fill="#f28a1c"/>
      <path d="M62 11 q6 -4 12 0 v2 h-3 v-1.5 q-3 -1 -6 0 v1.5 h-3 z" fill="#fff"/>
      <rect x="63.5" y="14" width="9" height="5" rx="1" fill="#fff"/>
      <rect x="89" y="9" width="12" height="8.5" rx="1" fill="#fff"/>
      <path d="M89.5 9.5 l5.5 4.5 l5.5 -4.5" fill="none" stroke="#f28a1c" stroke-width="1.2"/>
      <circle cx="122" cy="13" r="6" fill="none" stroke="#fff" stroke-width="1.5"/>
      <ellipse cx="122" cy="13" rx="2.6" ry="6" fill="none" stroke="#fff" stroke-width="1.2"/>
      <line x1="116" y1="13" x2="128" y2="13" stroke="#fff" stroke-width="1.2"/>
    </svg>

    <div class="contact-list centered" style="top:396px;">
      <p>0438 614 205</p>
      <p>desfairweather@balgogroundworks.com.au</p>
      <p>www.balgogroundworks.com.au</p>
    </div>

    <div class="rule" style="top:471px; left:89px; width:194px;"></div>

    <p class="company-label centered" style="top:488px;">BALGO GROUNDWORKS PTY LTD</p>
    <div class="address centered" style="top:507px;">
      <p>82 Dunmore Creek Road,</p>
      <p>Corrinvale NSW 2396</p>
    </div>
  </section>

  <section class="card card--back" aria-label="Business card, brand side">
    <div class="brand-name centered" style="top:180px;">
      <span class="brand-name__main">BALGO</span>
      <span class="brand-name__sub">GROUNDWORKS PTY LTD</span>
    </div>

    <p class="abn centered" style="top:321px;"><span class="abn__label">ABN</span> 58 402 917 364</p>

    <div class="rule" style="top:463px; left:65px; width:236px;"></div>

    <p class="specialty-label centered" style="top:480px;">WE SPECIALISE IN</p>
    <div class="specialties centered" style="top:499px;">
      <p>Agriculture, Civil Construction</p>
      <p>and Mining.</p>
    </div>
  </section>

</body>
</html>
```